Qamrin Advertising & Publicity business cards

I would like my Company's business card to be designed creatively & profissionally the logo is attached in both Arabic & english and prefer to have my emblem dimmed on the card as well
-Logo ( Arabic & English)
-Name (Arabic & English)
-Title ( Arabic & English)
-----------
-Location
-Landline (icon)
-Mobile phone (icon)
-Email (icon)
-Instagram (icon)
-WhatsApp (icon)

Target Market(s)

Industry/Entity Type

Marketing

Contact Information for Business Card

-Logo ( Arabic & English)
-Name (Arabic & English)
-----------
-Location
-Landline (icon)
-Mobile phone (icon)
-Email (icon)
-Instagram (icon)
-WhatsApp (icon)

Font styles to use
Serif

Requirements
Must have
• all what is mentions in business card details blanked and i will add the data my self
Nice to have
• Dim emblem on my business card both Arabic & english

```html
<!DOCTYPE html>
<html lang="en">
<head>
<meta charset="utf-8">
<title>Qamrin Advertising &amp; Publicity – Business Cards</title>
<link rel="stylesheet" href="https://fonts.googleapis.com/css2?family=Poppins:wght@400;500;600&family=Cairo:wght@600;700&display=swap">
<style>
  :root{
    --stage:#136b6c;
    --card-light:#ffffff;
    --card-tint:#d3ecec;
    --accent:#55c4c8;
    --accent-soft:#8fd8da;
    --ink:#111111;
    --emblem:#3fb7b6;
    --emblem-faint:rgba(120,190,190,.16);
  }
  *{margin:0;padding:0;box-sizing:border-box}
  html,body{width:1200px;height:1200px;overflow:hidden}
  body{background:var(--stage);position:relative;font-family:"Poppins",sans-serif;color:var(--ink)}

  .card{
    position:absolute;width:820px;height:470px;overflow:hidden;
    background:radial-gradient(ellipse at 38% 45%,var(--card-light) 0%,var(--card-light) 40%,var(--card-tint) 100%);
    box-shadow:0 18px 30px rgba(0,0,0,.35);
  }
  .card--english{left:80px;top:110px}
  .card--arabic{left:300px;top:620px}

  .corner-tab{position:absolute;top:0;left:88px;width:52px;height:60px;background:var(--accent-soft)}
  .contact-rail{
    position:absolute;left:88px;bottom:0;width:46px;height:230px;background:var(--accent);
    display:flex;flex-direction:column;align-items:center;justify-content:space-evenly;padding:10px 0;
  }
  .contact-rail svg{width:24px;height:24px}

  .emblem{position:absolute;background:var(--emblem);transform:rotate(45deg);border-radius:16px}
  .emblem-faint{
    position:absolute;width:430px;height:430px;transform:rotate(45deg);border-radius:60px;
    background:radial-gradient(circle,var(--emblem-faint) 0%,rgba(120,190,190,.08) 70%);
  }

  .divider{position:absolute;width:2px;background:var(--ink)}

  .wordmark{position:absolute;font-family:"Poppins",sans-serif;font-weight:500;font-size:80px;line-height:1;color:var(--ink);white-space:nowrap}
  .tagline{position:absolute;font-size:19px;font-weight:400;color:var(--ink);white-space:nowrap}
  .wordmark--arabic{font-family:"Cairo",sans-serif;font-weight:700;font-size:76px;line-height:1.2;direction:rtl;text-align:center;width:200px}
  .tagline--arabic{font-family:"Cairo",sans-serif;font-weight:700;font-size:20px;direction:rtl;text-align:center;width:200px}

  .identity{position:absolute;font-size:21px}
  .identity__name{display:flex;align-items:center;gap:8px;color:var(--accent);font-weight:600}
  .identity__title{display:flex;align-items:center;gap:8px;margin-top:2px;font-weight:400}
  .identity svg{width:20px;height:20px}
</style>
</head>
<body>

<section class="card card--english">
  <div class="emblem-faint" role="img" aria-label="Dimmed company emblem" style="left:400px;top:60px"></div>
  <div class="corner-tab"></div>
  <div class="emblem" role="img" aria-label="Company emblem" style="left:62px;top:115px;width:100px;height:100px"></div>
  <div class="divider" style="left:196px;top:58px;height:108px"></div>
  <div class="wordmark" style="left:212px;top:58px">Qamrin</div>
  <div class="tagline" style="left:214px;top:144px">Advertising and Publicity</div>
  <div class="divider" style="left:545px;top:50px;height:80px"></div>
  <div class="identity" style="left:560px;top:52px">
    <div class="identity__name"><svg viewBox="0 0 24 24"><circle cx="12" cy="8" r="5" fill="currentColor"/><path d="M3 22c0-5 4-8 9-8s9 3 9 8z" fill="currentColor"/></svg>Name</div>
    <div class="identity__title"><svg viewBox="0 0 24 24"><path d="M3 12h13M12 7l5 5-5 5" stroke="currentColor" stroke-width="2.5" fill="none"/></svg>title</div>
  </div>
  <nav class="contact-rail" aria-label="Contact details">
    <svg viewBox="0 0 24 24"><path d="M12 3 2 12h3v9h5v-6h4v6h5v-9h3z" fill="#111"/></svg>
    <svg viewBox="0 0 24 24"><rect x="5" y="3" width="14" height="18" rx="2" fill="#fff"/><path d="M8 8h8M8 12h8M8 16h5" stroke="#111" stroke-width="1.6"/></svg>
    <svg viewBox="0 0 24 24"><path d="M4 9c3-3 13-3 16 0l-2 3-3-1v-2c-2-.6-4-.6-6 0v2l-3 1z" fill="#111"/></svg>
    <svg viewBox="0 0 24 24"><rect x="3" y="6" width="18" height="12" fill="#fff"/><path d="M3 6l9 7 9-7" stroke="#888" stroke-width="1.4" fill="none"/></svg>
    <svg viewBox="0 0 24 24"><rect x="4" y="4" width="16" height="16" rx="3" fill="#fff"/></svg>
    <svg viewBox="0 0 24 24"><circle cx="12" cy="12" r="9" fill="#fff"/></svg>
  </nav>
</section>

<section class="card card--arabic">
  <div class="emblem-faint" role="img" aria-label="Dimmed company emblem" style="left:420px;top:80px"></div>
  <div class="corner-tab"></div>
  <div class="wordmark wordmark--arabic" style="left:155px;top:38px">قمرين</div>
  <div class="tagline tagline--arabic" style="left:155px;top:140px">للدعاية والإعلان</div>
  <div class="divider" style="left:375px;top:56px;height:104px"></div>
  <div class="emblem" role="img" aria-label="Company emblem" style="left:418px;top:66px;width:88px;height:88px"></div>
  <div class="divider" style="left:548px;top:50px;height:86px"></div>
  <div class="identity" style="left:563px;top:56px">
    <div class="identity__name"><svg viewBox="0 0 24 24"><circle cx="12" cy="8" r="5" fill="currentColor"/><path d="M3 22c0-5 4-8 9-8s9 3 9 8z" fill="currentColor"/></svg>Name</div>
    <div class="identity__title"><svg viewBox="0 0 24 24"><path d="M3 12h13M12 7l5 5-5 5" stroke="currentColor" stroke-width="2.5" fill="none"/></svg>title</div>
  </div>
  <nav class="contact-rail" aria-label="Contact details">
    <svg viewBox="0 0 24 24"><path d="M12 3 2 12h3v9h5v-6h4v6h5v-9h3z" fill="#111"/></svg>
    <svg viewBox="0 0 24 24"><rect x="5" y="3" width="14" height="18" rx="2" fill="#fff"/><path d="M8 8h8M8 12h8M8 16h5" stroke="#111" stroke-width="1.6"/></svg>
    <svg viewBox="0 0 24 24"><path d="M4 9c3-3 13-3 16 0l-2 3-3-1v-2c-2-.6-4-.6-6 0v2l-3 1z" fill="#111"/></svg>
    <svg viewBox="0 0 24 24"><rect x="3" y="6" width="18" height="12" fill="#fff"/><path d="M3 6l9 7 9-7" stroke="#888" stroke-width="1.4" fill="none"/></svg>
    <svg viewBox="0 0 24 24"><rect x="4" y="4" width="16" height="16" rx="3" fill="#fff"/></svg>
    <svg viewBox="0 0 24 24"><circle cx="12" cy="12" r="9" fill="#fff"/></svg>
  </nav>
</section>

</body>
</html>
```